Automotive debt collection business need several banners for new website

We are a debt recovery company called Kelvane Receivables Ltd who work specifically within the car automotive industry acting on behalf of our clients to recover debt which is owed to them. The advantage to using a company such as KVR is that it allows our clients the ability to outsource the work, removing the headache of dealing with the general public and reduces internal staff/overhead costs.
We collect various types of debt including:
Excess Mileage - this is charged when an individual has exceeded their permitted mileage allowance. This is calculated on a pence per mile basis on the mileage over the limit set when the contract was signed.
Damage - charged when a vehicle sustains more damage than is permitted within the contract. Damage could be dents to bodywork, large scratches, torn seats etc. Every area of damage over and above the allowed levels is detailed via a 'Damage Report' and a cost associated to that area of damage. The individual costs are then added up and a total charge formulated. The customer is liable to pay these charges as they have not cared for the vehicle in the appropriate manner whilst under their control
End of Contract Arrears - Once a contract ends and a vehicle is returned to our clients, there may be other charges that need to be repaid that remain outstanding.
We collect debt using a simple process. 1 - The customer is sent a letter as soon as the vehicle is collected advising them of the value of the debt. 2 - A few days later, we attempt to make contact via telephone or email. 3 - Once we contact the customer, we explain the debt and how the figure has been formulated (which is also explain in their letters). 4 - We negotiate (where appropriate) and agree a settlement figure. 5 - The customer pays the debt either in one installment over over a short payment plan.
Our new website (test URL only - http://testing.kelvanereceivables.co.uk/) has a dual purpose. Firstly its to help promote our services to new clients who may be in the market for an alternative supplier (as far as we are aware, we are the only dedicated automotive debt collection company in the UK) and secondly, as a site to help those who owe money to pay and understand who we are (and that we are a registered, legal debt collection company)
Unlike other debt collection websites, we do not want generic images of people shaking hands, smiling etc. We want the images to be visually striking and make the website stand out from the competition. We are happy for these to be graphics rather than images.
We require some visual banners to represent what we do as a business and to emphasis that we specifically collect debt for the automotive sector.
These are websites that contain banners that we are NOT looking for:
http://uk.zintaro-group.com/consumers/contact-data-working-hours/ - bland images of call centers/random people on phones etc
http://www.pellowmarsh.com/client/
These are websites that contain banners that we class as OK:
http://www.quorvath.co.uk/business-services/debt-collection.html - fairly clear way of explaining their services
http://www.estatearrears.co.uk/ - a slightly different slant using non-related images to explain what they can and cant do
http://www.wqlholdings.com/home/#.UhNNeD98CL0 - uses text to text banners to explain their offering
We require:
x4 - 870px X 500px - these will appear on the main homepage and rotate
x2 - 270px X 240px - static images that will to the right of the home page. One image needs to indicate some type of payment method as its a link to our online payment system, the second image refers to our other services (see the appropriate page on the website) these additional services include asset recovery, inspection, bespoke software solutions for the asset industry and auction disposal
x3 - 90px X 90px - Static images to represent payment methods that include cheque/card/bank transfer (see website for more info)
Our corporate colours are Black/Red/Grey
Depending on the designs received, we expect 2 rounds of modifications and we will advise those designers that have not been successful with positive feedback. We guarantee to pay the successful designer but work must be completed and ALL requested material produced and approved.

```html
<!DOCTYPE html>
<html lang="en">
<head>
<meta charset="utf-8">
<title>Kelvane Receivables Ltd</title>
<link rel="stylesheet" href="https://fonts.googleapis.com/css2?family=Arimo:wght@400;700&family=Jost:wght@600&family=Encode+Sans+Condensed:wght@300&display=swap">
<style>
  :root {
    --page-bg: #ffffff;
    --ink: #1d1d1d;
    --brand-red: #7a0c12;
    --bright-red: #c9202a;
    --accent-orange: #f07a2a;
    --portal-grey: #a2a9b2;
    --nav-grey: #676a73;
    --nav-dark: #5b5e66;
    --panel-grey: #7f8891;
    --white: #ffffff;
    --banner-dark: #141011;
  }
  * { box-sizing: border-box; margin: 0; padding: 0; }
  html, body { width: 1200px; height: 654px; overflow: hidden; background: var(--page-bg); }
  body { position: relative; font-family: "Arimo", Arial, sans-serif; border-top: 1px solid #000; }

  .page {
    position: absolute; left: 92px; top: 0; width: 1020px; height: 654px;
    background: var(--page-bg);
    box-shadow: 0 0 3px rgba(0,0,0,0.12);
  }

  .brand {
    position: absolute; left: 114px; top: 38px;
    display: flex; align-items: center; gap: 8px;
    color: var(--ink); font-size: 26px; font-weight: 400; letter-spacing: 0.5px;
    line-height: 1.1;
  }
  .brand-mark { width: 12px; height: 12px; background: var(--bright-red); border-radius: 50%; }
  .brand-name { display: block; }

  .portal-box {
    position: absolute; left: 840px; top: 18px; width: 255px; height: 92px;
    background: var(--portal-grey); border: 1px solid var(--brand-red);
    padding: 28px 0 0 17px; color: var(--brand-red);
  }
  .portal-title { font-size: 16px; font-weight: 700; }
  .portal-note { font-size: 12px; margin-top: 12px; }

  .main-nav {
    position: absolute; left: 109px; top: 137px; width: 986px; height: 50px;
    background: var(--nav-grey);
  }
  .nav-toggle {
    position: absolute; left: 0; top: 0; width: 32px; height: 50px;
    background: var(--nav-dark); color: var(--white); font-size: 11px;
    padding: 7px 0 0 5px;
  }
  .nav-link {
    position: absolute; top: 19px; color: var(--white); font-size: 12px; text-decoration: none;
  }

  .hero { position: absolute; left: 109px; top: 212px; width: 986px; height: 422px; }
  .hero-slide {
    position: absolute; left: 0; top: 0; width: 733px; height: 422px;
    background:
      radial-gradient(ellipse 260px 300px at 560px 230px, rgba(240,122,42,0.55), rgba(200,60,30,0.25) 55%, rgba(20,16,17,0) 75%),
      var(--banner-dark);
  }
  .slide-title {
    position: absolute; left: 37px; top: 20px;
    font-family: "Jost", "Futura", sans-serif; font-weight: 600;
    font-size: 52px; line-height: 0.98; color: var(--bright-red);
  }
  .slide-copy {
    position: absolute; left: 37px; top: 150px;
    font-family: "Encode Sans Condensed", sans-serif; font-weight: 300;
    font-size: 22px; line-height: 28px; color: var(--white);
  }
  .slide-copy .highlight { color: var(--accent-orange); }

  .hero-aside {
    position: absolute; left: 733px; top: 0; width: 253px; height: 422px;
    background: var(--panel-grey); color: var(--white); padding: 26px 0 0 25px;
  }
  .aside-heading { font-size: 19px; font-weight: 400; line-height: 23px; }
  .aside-heading strong { font-weight: 700; display: block; }
  .aside-text { margin-top: 14px; width: 205px; font-size: 11.4px; line-height: 17.7px; }
  .all-posts {
    position: absolute; left: 25px; top: 313px; width: 105px; height: 34px;
    background: var(--brand-red); color: var(--white); text-decoration: none;
    font-size: 10px; font-weight: 700; letter-spacing: 0.3px;
    display: flex; align-items: center; justify-content: center; gap: 9px;
  }
  .slider-btn {
    position: absolute; top: 371px; width: 26px; height: 25px;
    background: var(--brand-red); display: flex; align-items: center; justify-content: center;
  }
  .slider-prev { left: 168px; }
  .slider-next { left: 202px; }
</style>
</head>
<body>
  <div class="page"></div>

  <div class="brand">
    <span class="brand-name">KVR receivables</span>
    <span class="brand-mark"></span>
  </div>

  <aside class="portal-box">
    <h2 class="portal-title">Customer Portal</h2>
    <p class="portal-note">Our customer portal is comming soon</p>
  </aside>

  <nav class="main-nav">
    <span class="nav-toggle">~</span>
    <a class="nav-link" href="#" style="left:53px">About Us</a>
    <a class="nav-link" href="#" style="left:143px">Features</a>
    <a class="nav-link" href="#" style="left:233px">Additional Services</a>
    <a class="nav-link" href="#" style="left:376px">FAQ</a>
    <a class="nav-link" href="#" style="left:442px">Payment Portal</a>
    <a class="nav-link" href="#" style="left:569px">Contact Us</a>
  </nav>

  <section class="hero">
    <div class="hero-slide" role="img" aria-label="Speedometer illustration with glowing orange dial and needle past 160 on a dark textured background">
      <h1 class="slide-title">Excess<br>Mileage</h1>
      <p class="slide-copy">Calculated on a <span class="highlight">pence per mile</span> basis<br>on the mileage over the limit set<br>when the contract was signed</p>
    </div>

    <div class="hero-aside">
      <h2 class="aside-heading">HAPPY<br>CUSTOMERS<strong>BUY NOW</strong></h2>
      <p class="aside-text">Mauris gravida vulputate ligula, ut sagittis libero consequat nec. Morbi mi sapien, viverra non interdum rutrum, viverra et massa. Suspendisse potenti. Vivamus orci nibh, egestas ac adipiscing id, tempus in justo. Duis blandit volutpat nunc nec dictum. Sed eget lectus sed est condimentum ultricies ut quis nunc. Aliquam mollis interdum condimentum.</p>
      <a class="all-posts" href="#">ALL POSTS
        <svg width="9" height="9" viewBox="0 0 9 9" aria-hidden="true"><path d="M3 1l4 3.5L3 8" fill="none" stroke="#fff" stroke-width="1.5"/></svg>
      </a>
      <a class="slider-btn slider-prev" href="#" aria-label="Previous slide">
        <svg width="9" height="10" viewBox="0 0 9 10" aria-hidden="true"><path d="M6.5 1L2.5 5l4 4" fill="none" stroke="#fff" stroke-width="1.6"/></svg>
      </a>
      <a class="slider-btn slider-next" href="#" aria-label="Next slide">
        <svg width="9" height="10" viewBox="0 0 9 10" aria-hidden="true"><path d="M2.5 1l4 4-4 4" fill="none" stroke="#fff" stroke-width="1.6"/></svg>
      </a>
    </div>
  </section>
</body>
</html>
```